Cosmetic injections clinic needs a fresh looking business card

We need a business card using the supplied logo and color scheme to attract future clients to our clinic. It should be modern and fresh, eye catching and not too busy. Simple and to the point is best. I would like two sided designs with the front indicating address and contact information, and the back in full color with white logo and descriptive information also provided.
Target Market(s)
Clients looking for non surgical beauty enhancements.
Contact Information for Business Card
MeloraSkin
14, 618 Birchmont Way
Cedarvale, Ontario
K2P 7W3
Phone: 587-412-6630
Email: info@meloraskin.com
Requirements
Must have
- -Logo supplied with the name and address of the clinic
- -Back of card in full color with white logo with A small line of text indicating both of the following: Anti aging consultants and cosmetic injectables
- Located inside the Voyager Wellness Group

```html
<!DOCTYPE html>
<html lang="en">
<head>
<meta charset="utf-8">
<title>MeloraSkin Business Cards</title>
<link href="https://fonts.googleapis.com/css2?family=Questrial&family=Montserrat:wght@600&display=swap" rel="stylesheet">
<style>
  :root {
    --stage: #626262;
    --pink: #e44595;
    --purple: #6b459c;
    --teal: #29bdbb;
    --ink: #3a3a3a;
    --rule: #555555;
    --paper-centre: #ffffff;
    --paper-edge: #dfe1e3;
    --white: #ffffff;
  }
  * { margin: 0; padding: 0; box-sizing: border-box; }
  html, body { width: 1051px; height: 1200px; overflow: hidden; }
  body {
    position: relative;
    background: var(--stage);
    font-family: "Questrial", sans-serif;
    color: var(--ink);
  }
  .card { position: absolute; width: 342px; height: 196px; }
  .card-front {
    left: 161px;
    background: radial-gradient(ellipse at 40% 50%, var(--paper-centre) 0%, #f4f5f6 45%, var(--paper-edge) 100%);
  }
  .card-back { left: 555px; color: var(--white); text-align: center; }
  .row-1 { top: 160px; }
  .row-2 { top: 490px; }
  .row-3 { top: 820px; }
  .back-pink { background: var(--pink); }
  .back-purple { background: var(--purple); }
  .back-teal { background: var(--teal); }

  .brand {
    position: absolute;
    display: flex;
    align-items: center;
    gap: 6px;
    font-family: "Montserrat", sans-serif;
    font-weight: 600;
    white-space: nowrap;
  }
  .brand-dot { border-radius: 50%; flex: none; }
  .card-front .brand { left: 28px; top: 86px; font-size: 15px; color: var(--purple); }
  .card-front .brand-dot { width: 20px; height: 20px; background: var(--pink); }
  .card-back .brand {
    left: 0; right: 0; top: 70px; justify-content: center;
    font-size: 21px; color: var(--white);
  }
  .card-back .brand-dot { width: 28px; height: 28px; background: var(--white); }

  .divider {
    position: absolute; left: 170px; top: 39px;
    width: 1px; height: 118px; background: var(--rule);
  }
  .details { position: absolute; left: 185px; top: 41px; }
  .clinic-name { font-size: 14.5px; line-height: 1; }
  .clinic-sub { font-size: 7.5px; letter-spacing: 0.3px; margin-top: 2px; color: var(--ink); }
  .contact-list { list-style: none; margin-top: 23px; font-size: 9.6px; line-height: 1.2; color: var(--ink); }
  .contact-list li { display: flex; gap: 5px; margin-bottom: 5px; }
  .contact-list svg { width: 8px; height: 8px; flex: none; margin-top: 2px; }
  .accent-pink { --accent: var(--pink); }
  .accent-purple { --accent: var(--purple); }
  .accent-teal { --accent: var(--teal); }
  .clinic-name { color: var(--accent); }
  .icon-box { fill: var(--accent); }

  .back-rule {
    position: absolute; left: 160px; top: 131px;
    width: 22px; height: 1px; background: var(--white);
  }
  .tagline {
    position: absolute; left: 0; right: 0; top: 142px;
    font-size: 9.6px; line-height: 18px;
  }
</style>
</head>
<body>

  <section class="card card-front row-1 accent-pink">
    <div class="brand"><span class="brand-dot"></span>MeloraSkin</div>
    <div class="divider"></div>
    <div class="details">
      <p class="clinic-name">MeloraSkin</p>
      <p class="clinic-sub">COSMETIC CLINIC</p>
      <ul class="contact-list">
        <li><svg viewBox="0 0 8 8"><rect class="icon-box" width="8" height="8" rx="1"/><path d="M2 2l1 0 .6 1.3-.6.5a3 3 0 0 0 1.2 1.2l.5-.6L6 5v1c-2 .3-4.3-2-4-4z" fill="#fff"/></svg>555.412.6630</li>
        <li><svg viewBox="0 0 8 8"><rect class="icon-box" width="8" height="8" rx="1"/><rect x="1.6" y="2.4" width="4.8" height="3.2" fill="#fff"/></svg>info@meloraskin.com</li>
        <li><svg viewBox="0 0 8 8"><rect class="icon-box" width="8" height="8" rx="1"/><path d="M4 1.5a1.8 1.8 0 0 1 1.8 1.8C5.8 4.6 4 6.5 4 6.5S2.2 4.6 2.2 3.3A1.8 1.8 0 0 1 4 1.5z" fill="#fff"/></svg><span>14, 618 Birchmont Way<br>Cedarvale, Ontario<br>K2P 7W3</span></li>
      </ul>
    </div>
  </section>
  <section class="card card-back row-1 back-pink">
    <div class="brand"><span class="brand-dot"></span>MeloraSkin</div>
    <div class="back-rule"></div>
    <p class="tagline">Anti aging consultants and cosmetic injectables<br>Located inside the Voyager Wellness Group</p>
  </section>

  <section class="card card-front row-2 accent-purple">
    <div class="brand"><span class="brand-dot"></span>MeloraSkin</div>
    <div class="divider"></div>
    <div class="details">
      <p class="clinic-name">MeloraSkin</p>
      <p class="clinic-sub">COSMETIC CLINIC</p>
      <ul class="contact-list">
        <li><svg viewBox="0 0 8 8"><rect class="icon-box" width="8" height="8" rx="1"/><path d="M2 2l1 0 .6 1.3-.6.5a3 3 0 0 0 1.2 1.2l.5-.6L6 5v1c-2 .3-4.3-2-4-4z" fill="#fff"/></svg>555.412.6630</li>
        <li><svg viewBox="0 0 8 8"><rect class="icon-box" width="8" height="8" rx="1"/><rect x="1.6" y="2.4" width="4.8" height="3.2" fill="#fff"/></svg>info@meloraskin.com</li>
        <li><svg viewBox="0 0 8 8"><rect class="icon-box" width="8" height="8" rx="1"/><path d="M4 1.5a1.8 1.8 0 0 1 1.8 1.8C5.8 4.6 4 6.5 4 6.5S2.2 4.6 2.2 3.3A1.8 1.8 0 0 1 4 1.5z" fill="#fff"/></svg><span>14, 618 Birchmont Way<br>Cedarvale, Ontario<br>K2P 7W3</span></li>
      </ul>
    </div>
  </section>
  <section class="card card-back row-2 back-purple">
    <div class="brand"><span class="brand-dot"></span>MeloraSkin</div>
    <div class="back-rule"></div>
    <p class="tagline">Anti aging consultants and cosmetic injectables<br>Located inside the Voyager Wellness Group</p>
  </section>

  <section class="card card-front row-3 accent-teal">
    <div class="brand"><span class="brand-dot"></span>MeloraSkin</div>
    <div class="divider"></div>
    <div class="details">
      <p class="clinic-name">MeloraSkin</p>
      <p class="clinic-sub">COSMETIC CLINIC</p>
      <ul class="contact-list">
        <li><svg viewBox="0 0 8 8"><rect class="icon-box" width="8" height="8" rx="1"/><path d="M2 2l1 0 .6 1.3-.6.5a3 3 0 0 0 1.2 1.2l.5-.6L6 5v1c-2 .3-4.3-2-4-4z" fill="#fff"/></svg>555.412.6630</li>
        <li><svg viewBox="0 0 8 8"><rect class="icon-box" width="8" height="8" rx="1"/><rect x="1.6" y="2.4" width="4.8" height="3.2" fill="#fff"/></svg>info@meloraskin.com</li>
        <li><svg viewBox="0 0 8 8"><rect class="icon-box" width="8" height="8" rx="1"/><path d="M4 1.5a1.8 1.8 0 0 1 1.8 1.8C5.8 4.6 4 6.5 4 6.5S2.2 4.6 2.2 3.3A1.8 1.8 0 0 1 4 1.5z" fill="#fff"/></svg><span>14, 618 Birchmont Way<br>Cedarvale, Ontario<br>K2P 7W3</span></li>
      </ul>
    </div>
  </section>
  <section class="card card-back row-3 back-teal">
    <div class="brand"><span class="brand-dot"></span>MeloraSkin</div>
    <div class="back-rule"></div>
    <p class="tagline">Anti aging consultants and cosmetic injectables<br>Located inside the Voyager Wellness Group</p>
  </section>

</body>
</html>
```